hawkiron structural steel

8 1/2" x 11" flyer color both sides. Use at least 12 pictures.

Add the word; structural under HawkIron to logo

bullet points:
Laser Accuracy
On-time scheduling
Own our Equipment
39 Years Exp.
Manufacturing Construction Brackets Since 1982
We manufacture custom ibeams in Phoenix, AZ
Certified welders

Hawkiron Plant
4812 n. 27th street, suite-3
Phx, AZ 85019
480-926-8147

Target Market(s)

Architects, builders

Industry/Entity Type

construction

Colors
0054AA
0677BA
7BADD7
CADEEF
E8F1F8

```html
<!DOCTYPE html>
<html lang="en">
<head>
<meta charset="utf-8">
<title>HawkIron Structural Steel Flyer</title>
<link rel="stylesheet" href="https://fonts.googleapis.com/css2?family=Oswald:wght@300;400;500;600&family=Roboto+Condensed:wght@400;700&display=swap">
<style>
  :root {
    --stage: #474747;
    --brand-blue: #1d57aa;
    --mid-blue: #0677ba;
    --sky-blue: #7badd7;
    --pale-blue: #cadeef;
    --ice-blue: #e8f1f8;
    --periwinkle: #8ea4d9;
    --logo-box: #4a6aa8;
    --white: #ffffff;
  }
  * { margin: 0; padding: 0; box-sizing: border-box; }
  html, body { width: 1200px; height: 1000px; overflow: hidden; background: var(--stage); }
  .canvas { position: relative; width: 1200px; height: 1000px; }
  .page { position: absolute; top: 209px; width: 449px; height: 581px; background: var(--white); overflow: hidden; }
  .page--front { left: 110px; }
  .page--back { left: 640px; }
  .abs { position: absolute; }
  .photo { position: absolute; }
  .brand-name { font-family: 'Oswald', sans-serif; font-weight: 400; color: var(--white); letter-spacing: 0.5px; white-space: nowrap; display: block; }
  .brand-tag { font-family: 'Oswald', sans-serif; font-weight: 400; color: var(--white); letter-spacing: 1.5px; white-space: nowrap; display: block; }

  /* front page */
  .front-sky-band { left: 0; top: 0; width: 449px; height: 79px; background: var(--periwinkle); }
  .front-hero { left: 0; top: 79px; width: 449px; height: 311px;
    background: linear-gradient(180deg, #8a9cd4 0%, #7a86c4 35%, #b08cc6 55%, #d9a0c8 62%, #4f5f93 72%, #3c4d80 100%); }
  .front-logo-box { left: 294px; top: 0; width: 92px; height: 79px; background: var(--logo-box);
    display: flex; flex-direction: column; align-items: center; justify-content: flex-end; padding-bottom: 10px; text-align: center; }
  .front-logo-box .brand-name { font-size: 12px; line-height: 14px; }
  .front-logo-box .brand-tag { font-size: 7px; line-height: 9px; }
  .front-title-box { left: 0; top: 79px; width: 294px; height: 78px; background: var(--white); }
  .front-title { position: absolute; left: 44px; top: 7px; font-family: 'Oswald', sans-serif; font-weight: 600;
    font-size: 38px; line-height: 46px; color: var(--brand-blue); letter-spacing: -0.6px; white-space: nowrap; }
  .front-subtitle { position: absolute; left: 44px; top: 52px; font-family: 'Roboto Condensed', sans-serif;
    font-size: 13px; color: var(--brand-blue); }
  .service-line { left: 44px; top: 160px; font-family: 'Roboto Condensed', sans-serif; font-size: 12px;
    color: var(--white); white-space: nowrap; }
  .service-line span { margin: 0 5px; }
  .front-strip-photo { top: 398px; height: 86px; }
  .front-footer { left: 0; top: 490px; width: 449px; height: 91px; background: var(--brand-blue); color: var(--white); }
  .footer-heading { position: absolute; left: 60px; top: 11px; font-family: 'Oswald', sans-serif; font-weight: 400;
    font-size: 21px; letter-spacing: 1.5px; }
  .footer-line { position: absolute; left: 60px; font-family: 'Roboto Condensed', sans-serif; font-weight: 700; font-size: 9.5px; }
  .footer-since { position: absolute; right: 31px; top: 49px; font-family: 'Oswald', sans-serif; font-weight: 300; font-size: 18px; }

  /* back page */
  .back-hero { left: 0; top: 0; width: 249px; height: 207px;
    background: linear-gradient(180deg, #9fc0e0 0%, #c9d9e8 45%, #a88a78 68%, #7c7a78 100%); }
  .back-panel { left: 249px; top: 0; width: 200px; height: 328px; background: var(--brand-blue); }
  .back-logo { left: 249px; top: 84px; width: 200px; text-align: center; }
  .back-logo .brand-name { font-size: 15px; line-height: 17px; }
  .back-logo .brand-tag { font-size: 8px; line-height: 10px; }
  .back-logo-dot { display: inline-block; width: 8px; height: 8px; border-radius: 50%; background: var(--white); margin-right: 5px; vertical-align: middle; }
  .back-title { left: 283px; top: 132px; font-family: 'Oswald', sans-serif; font-weight: 500; font-size: 37px;
    line-height: 37px; color: var(--white); letter-spacing: -0.5px; }
  .experience-bar { left: 274px; top: 256px; width: 175px; height: 42px; background: var(--mid-blue); color: var(--white);
    font-family: 'Oswald', sans-serif; font-weight: 400; padding: 5px 0 0 11px; line-height: 15px; }
  .experience-bar .years { font-size: 16px; display: block; margin-bottom: 2px; }
  .experience-bar .word { font-size: 13px; }
  .back-footer-band { left: 0; top: 506px; width: 449px; height: 75px; background: var(--brand-blue); }
  .grid-photo { position: absolute; }
  .feature { position: absolute; width: 80px; text-align: center; }
  .feature-icon { display: block; margin: 0 auto; }
  .feature-label { font-family: 'Roboto Condensed', sans-serif; font-weight: 700; font-size: 10px; line-height: 11px;
    color: var(--brand-blue); margin-top: 3px; }
  .contact { left: 249px; top: 522px; width: 200px; text-align: center; color: var(--white); }
  .contact-phone { font-family: 'Oswald', sans-serif; font-weight: 500; font-size: 22px; line-height: 24px; display: flex; align-items: center; justify-content: center; gap: 6px; }
  .contact-plant { font-family: 'Roboto Condensed', sans-serif; font-weight: 700; font-size: 9px; margin-top: 2px; }
  .contact-address { font-family: 'Roboto Condensed', sans-serif; font-size: 7px; margin-top: 1px; }
</style>
</head>
<body>
<div class="canvas">

  <section class="page page--front">
    <div class="abs front-sky-band"></div>
    <div class="photo front-hero" role="img" aria-label="Steel frame structure at dusk on a desert building site with a telehandler under lights"></div>
    <div class="abs front-logo-box"><span class="brand-name">HAWK IRON</span><span class="brand-tag">STRUCTURAL</span></div>
    <div class="abs front-title-box">
      <h1 class="front-title">Structural Steel</h1>
      <p class="front-subtitle">39 Years Experieance</p>
    </div>
    <p class="abs service-line">DESIGN<span>|</span>FABRICATION<span>|</span>SUPPLY<span>|</span>INSTALLATION</p>

    <div class="photo front-strip-photo" style="left:0;width:142px;background:linear-gradient(180deg,#5c8fd0 0%,#8a6a4c 45%,#a89b86 100%)" role="img" aria-label="Curved steel roof framing with wood decking"></div>
    <div class="photo front-strip-photo" style="left:146px;width:164px;background:linear-gradient(180deg,#bfb6a8 0%,#7c94b8 50%,#5a7a4a 100%)" role="img" aria-label="Arched steel beams seen from below"></div>
    <div class="photo front-strip-photo" style="left:313px;width:136px;background:linear-gradient(180deg,#6b4e36 0%,#9db8d8 50%,#5a6a4a 100%)" role="img" aria-label="Finished curved canopy over a patio"></div>

    <div class="abs front-footer">
      <p class="footer-heading">We manufacture</p>
      <p class="footer-line" style="top:50px">Custom Ibeams Phoenix, AZ</p>
      <p class="footer-line" style="top:64px">Construction Brackets</p>
      <p class="footer-since">Since 1982</p>
    </div>
  </section>

  <section class="page page--back">
    <div class="photo back-hero" role="img" aria-label="Telehandler parked beneath a steel beam grid with red rocks behind"></div>
    <div class="abs back-panel"></div>
    <div class="abs back-logo"><span class="brand-name"><span class="back-logo-dot"></span>HAWK IRON</span><span class="brand-tag">STRUCTURAL</span></div>
    <h2 class="abs back-title">Structural<br>Steel<br>Expert</h2>
    <div class="abs experience-bar"><span class="years">39 Years</span><span class="word">Experieance</span></div>

    <div class="abs back-footer-band"></div>

    <div class="grid-photo" style="left:13px;top:218px;width:225px;height:110px;background:linear-gradient(180deg,#c9a878 0%,#5a8fd0 40%,#4f7a45 70%,#9a9a9a 100%)" role="img" aria-label="Worker checking arched steel canopy framing"></div>
    <div class="grid-photo" style="left:13px;top:334px;width:110px;height:111px;background:linear-gradient(180deg,#8c6a48 0%,#7fa8d8 55%,#5a7a4a 100%)" role="img" aria-label="Curved roof beams with wood slats"></div>
    <div class="grid-photo" style="left:128px;top:334px;width:110px;height:111px;background:linear-gradient(180deg,#1f6ad0 0%,#78aee0 70%,#4a5a6a 100%)" role="img" aria-label="Steel frame corner against blue sky"></div>
    <div class="grid-photo" style="left:13px;top:451px;width:110px;height:111px;background:linear-gradient(180deg,#d8e2ec 0%,#5a4a3c 45%,#9a6a4a 100%)" role="img" aria-label="Steel posts inside a timber-framed building"></div>
    <div class="grid-photo" style="left:128px;top:451px;width:110px;height:111px;background:linear-gradient(180deg,#4e8ad8 0%,#8ab0d8 45%,#c8d0d8 100%)" role="img" aria-label="Steel beams over a flooded foundation slab"></div>

    <div class="feature" style="left:265px;top:347px">
      <svg class="feature-icon" width="42" height="42" viewBox="0 0 42 42"><circle cx="21" cy="21" r="20" fill="#cadeef" stroke="#e8f1f8" stroke-width="2"/><rect x="13" y="11" width="15" height="20" fill="none" stroke="#1d57aa" stroke-width="1.3"/><path d="M16 21l4-4 4 4v5h-8z" fill="none" stroke="#1d57aa" stroke-width="1.2"/><path d="M26 27l6-10" stroke="#1d57aa" stroke-width="1.5"/></svg>
      <p class="feature-label">ON-TIME<br>SCHEDULING</p>
    </div>
    <div class="feature" style="left:339px;top:347px">
      <svg class="feature-icon" width="42" height="42" viewBox="0 0 42 42"><circle cx="21" cy="21" r="20" fill="#cadeef" stroke="#e8f1f8" stroke-width="2"/><path d="M13 20a8 8 0 0 1 16 0z" fill="none" stroke="#1d57aa" stroke-width="1.3"/><path d="M11 20h20M19 12h4v4h-4z" fill="none" stroke="#1d57aa" stroke-width="1.3"/><path d="M13 33v-6h16v6" fill="none" stroke="#1d57aa" stroke-width="1.3"/></svg>
      <p class="feature-label">CERTIFIED<br>WELDERS</p>
    </div>
    <div class="feature" style="left:265px;top:425px">
      <svg class="feature-icon" width="42" height="42" viewBox="0 0 42 42"><circle cx="21" cy="21" r="20" fill="#cadeef" stroke="#e8f1f8" stroke-width="2"/><rect x="17" y="9" width="8" height="10" fill="none" stroke="#1d57aa" stroke-width="1.3"/><circle cx="21" cy="14" r="2" fill="none" stroke="#1d57aa" stroke-width="1.2"/><path d="M21 19v14M21 19l-7 14M21 19l7 14" stroke="#1d57aa" stroke-width="1.3" fill="none"/></svg>
      <p class="feature-label">LASER<br>ACCURACY</p>
    </div>
    <div class="feature" style="left:339px;top:425px">
      <svg class="feature-icon" width="42" height="42" viewBox="0 0 42 42"><circle cx="21" cy="21" r="20" fill="#cadeef" stroke="#e8f1f8" stroke-width="2"/><path d="M12 30l14-14M25 12a4 4 0 1 0 5 5" stroke="#1d57aa" stroke-width="1.5" fill="none"/><path d="M30 30L16 16M13 12l4 4-3 3-4-4z" stroke="#1d57aa" stroke-width="1.5" fill="none"/></svg>
      <p class="feature-label">OWN OUR<br>EQUIPMENT</p>
    </div>

    <div class="abs contact">
      <p class="contact-phone"><svg width="15" height="15" viewBox="0 0 16 16"><rect x="0" y="0" width="16" height="16" rx="4" fill="#fff"/><path d="M5 3.5l2 2-1 1.5c.8 1.6 1.9 2.7 3.5 3.5L11 9.5l2 2-1.5 1.5C7.5 12.5 3.5 8.5 3 4.5z" fill="#1d57aa"/></svg>480-926-8147</p>
      <p class="contact-plant">Hawkiron Plant,</p>
      <p class="contact-address">4812 n. 27th street, suite-3 &nbsp;&nbsp; Phx, AZ 85019</p>
    </div>
  </section>

</div>
</body>
</html>
```